Update our OBGYN business card look and info

We are an OBGYN office. Our logo is nice but would like to "woman" part of the logo to be a darker color, to contrast with the flower that surrounds it. Maybe make our practice name Harbor Bloom Care Clinic more feminine. Our practice caters to women only. All providers and staff are female.

Target Market(s)

Females 16-65.

Industry/Entity Type

Business

Contact Information for Business Card

See attached upload. The ONLY CHANGE to the information is DELETE the name Dorothy Kemplin, Midwife and REPLACE with Greta Poundsworth, Midwife

Logo Text

Harbor Bloom Care Clinic Obstetrics & Gynecology

Font styles to use
Serif
Script

Colors
85cae6
0692cd
33a6d7
85abd2
f59195
eea4c8
cadf82
fac994
d3a5cc

```html
<!DOCTYPE html>
<html lang="en">
<head>
<meta charset="utf-8">
<title>Harbor Bloom Care Clinic – Business Cards</title>
<link href="https://fonts.googleapis.com/css2?family=Playfair+Display:wght@500&family=Raleway:wght@400;500&display=swap" rel="stylesheet">
<style>
  :root {
    --bg: #ececea;
    --paper: #f4f4f4;
    --blue-deep: #0692cd;
    --blue-light: #33a6d7;
    --pink: #f59195;
    --pink-soft: #e8a0a4;
    --ink-white: #ffffff;
  }
  * { margin: 0; padding: 0; box-sizing: border-box; }
  html, body { width: 1200px; height: 800px; overflow: hidden; }
  body {
    background: var(--bg);
    font-family: "Raleway", Arial, sans-serif;
    display: flex;
    align-items: center;
    justify-content: center;
    gap: 40px;
  }
  .card {
    position: relative;
    width: 540px;
    height: 309px;
    background: var(--paper);
    overflow: hidden;
    box-shadow: 0 10px 26px rgba(0,0,0,0.14);
  }
  .card-shapes { position: absolute; inset: 0; width: 100%; height: 100%; }

  .brand {
    position: absolute;
    display: flex;
    align-items: center;
    gap: 10px;
  }
  .brand-dot {
    width: 20px; height: 20px;
    border-radius: 50%;
    background: var(--pink);
    flex: none;
  }
  .brand-name {
    font-family: "Playfair Display", Georgia, serif;
    font-weight: 500;
    color: var(--blue-deep);
    letter-spacing: 0.3px;
    white-space: nowrap;
  }

  /* Front */
  .card-front .brand { left: 86px; top: 124px; }
  .card-front .brand-name { font-size: 30px; }
  .website {
    position: absolute;
    right: 62px; top: 190px;
    font-size: 16px;
    color: var(--blue-deep);
    letter-spacing: 0.3px;
  }

  /* Back */
  .card-back .brand { left: 28px; top: 62px; }
  .card-back .brand-dot { width: 15px; height: 15px; }
  .card-back .brand-name { font-size: 20px; }
  .providers {
    position: absolute;
    right: 24px; top: 118px;
    list-style: none;
    text-align: right;
    color: var(--ink-white);
    font-size: 14px;
    line-height: 1.45;
  }
  .contact {
    position: absolute;
    left: 28px; bottom: 20px;
    list-style: none;
    color: var(--ink-white);
    font-size: 13px;
    line-height: 1.4;
  }
  .contact li { display: flex; align-items: flex-start; gap: 8px; }
  .contact svg { width: 11px; height: 11px; margin-top: 4px; flex: none; fill: var(--ink-white); }
  .contact .address { display: block; }
</style>
</head>
<body>

  <section class="card card-front" aria-label="Business card front">
    <svg class="card-shapes" viewBox="0 0 540 309" preserveAspectRatio="none" aria-hidden="true">
      <polygon points="430,0 540,0 540,64 470,26" fill="var(--pink-soft)"/>
      <polygon points="440,0 540,0 540,56" fill="var(--blue-light)"/>
      <polygon points="0,250 0,309 120,309" fill="var(--blue-light)"/>
      <polygon points="0,256 0,309 104,309" fill="var(--pink-soft)"/>
    </svg>
    <div class="brand">
      <span class="brand-dot"></span>
      <span class="brand-name">Harbor Bloom Care Clinic</span>
    </div>
    <p class="website">www.harborbloomcare.com</p>
  </section>

  <section class="card card-back" aria-label="Business card back">
    <svg class="card-shapes" viewBox="0 0 540 309" preserveAspectRatio="none" aria-hidden="true">
      <defs>
        <linearGradient id="backBlue" x1="0" y1="0" x2="0" y2="1">
          <stop offset="0" stop-color="var(--blue-light)"/>
          <stop offset="1" stop-color="var(--blue-deep)"/>
        </linearGradient>
      </defs>
      <rect width="540" height="309" fill="url(#backBlue)"/>
      <polygon points="0,0 372,0 262,170 0,160" fill="var(--pink-soft)"/>
      <polygon points="0,0 362,0 256,163 0,154" fill="var(--paper)"/>
    </svg>
    <div class="brand">
      <span class="brand-dot"></span>
      <span class="brand-name">Harbor Bloom Care Clinic</span>
    </div>
    <ul class="providers">
      <li>Marian Selwick, MD</li>
      <li>Lena Ashcombe, MD</li>
      <li>Ruth Delacorte, MD</li>
      <li>Greta Poundsworth, Midwife</li>
      <li>Nora Penbrook, Midwife</li>
    </ul>
    <ul class="contact">
      <li>
        <svg viewBox="0 0 12 12" aria-hidden="true"><path d="M2.5 0.5 4.3 2.6 3.3 4.1C4 5.6 6.1 7.8 7.9 8.7L9.4 7.7 11.5 9.5 10.4 11.3C6.2 11.6 0.4 5.8 0.7 1.6Z"/></svg>
        <span>555-014-2290</span>
      </li>
      <li>
        <svg viewBox="0 0 12 12" aria-hidden="true"><path d="M3 0h6v3H3zM1 4h10v5H9v3H3V9H1zM4 8v3h4V8z"/></svg>
        <span>555-014-2291</span>
      </li>
      <li>
        <svg viewBox="0 0 12 12" aria-hidden="true"><path d="M0 2h12v8H0zM1 3v.4L6 6.6 11 3.4V3z"/></svg>
        <span>hello@harborbloomcare.com</span>
      </li>
      <li>
        <svg viewBox="0 0 12 12" aria-hidden="true"><path d="M6 0.5 11.5 5.5H10V11.5H7.3V8H4.7V11.5H2V5.5H0.5Z"/></svg>
        <span><span class="address">418 Willowmere Ave. Ste 3B</span><span class="address">Larkfield, OR 97000 1204</span></span>
      </li>
    </ul>
  </section>

</body>
</html>
```